Adventure Business Cards

Please check out our website for style
Vertical card
Details:
Side 1
Logo
Business name: Kestrel Bay Wildlife Tours
Name: Colin Marsby
Role: Director
Email: info@kestrelbaywildtours.example
Address: PO Box 71, Fennick Point NSW 2741
Phone: +61 2 5550 4817
Web address: www.kestrelbaywildtours.example
Side 2
Taking pictures?
A Facebook and Instagram logo
Tag us in your pictures with
#kbwildtoursco
@kbwildtoursco
www.kestrelbaywildtours.example
Details:
Side 1
Logo
Name: Colin Marsby
Role: Director
Phone: +61 2 5550 4817
Side 2
Taking pictures?
#kbwildtoursco
@kbwildtoursco

```html
<!DOCTYPE html>
<html lang="en">
<head>
<meta charset="utf-8">
<title>Kestrel Bay Wildlife Tours – Business Cards</title>
<link href="https://fonts.googleapis.com/css2?family=Share+Tech+Mono&family=Yanone+Kaffeesatz:wght@300;400&display=swap" rel="stylesheet">
<style>
  :root {
    --backdrop: #dcdcdc;
    --card-light: #ebebeb;
    --orange: #d9903a;
    --blue: #2c7cbf;
    --ink: #1e1e1e;
    --white: #ffffff;
  }
  * { box-sizing: border-box; margin: 0; padding: 0; }
  html, body { width: 1200px; height: 782px; overflow: hidden; }
  body { background: var(--backdrop); position: relative; }

  .card {
    position: absolute;
    background: var(--card-light);
    border-radius: 12px;
    overflow: hidden;
    box-shadow: 0 2px 6px rgba(0,0,0,0.12);
  }

  /* Back side (landscape) */
  .card--back { left: 132px; top: 340px; width: 556px; height: 310px; }
  .brand-mark {
    position: absolute; left: 146px; transform: translateX(-50%);
    display: flex; flex-direction: column; align-items: center;
  }
  .card--back .brand-mark { top: 46px; }
  .brand-disc { width: 140px; height: 140px; border-radius: 50%; background: var(--ink); }
  .brand-name {
    font-family: "Yanone Kaffeesatz", sans-serif; font-weight: 400;
    font-size: 22px; letter-spacing: 1px; text-transform: uppercase;
    color: var(--ink); margin-top: 12px; white-space: nowrap; text-align: center; line-height: 1.1;
  }

  .rotated {
    position: absolute; white-space: nowrap;
    transform: translate(-50%, -50%) rotate(-90deg);
  }
  .prompt-title {
    left: 378px; top: 154px;
    font-family: "Share Tech Mono", monospace; font-size: 26px;
    letter-spacing: 2px; color: var(--orange);
  }
  .prompt-line {
    left: 418px; top: 158px;
    font-family: "Yanone Kaffeesatz", sans-serif; font-weight: 400;
    font-size: 19px; color: var(--blue);
  }
  .social-tag {
    font-family: "Yanone Kaffeesatz", sans-serif; font-weight: 300;
    font-size: 18px; color: var(--blue); top: 155px;
  }
  .social-tag--hash { left: 440px; }
  .social-tag--handle { left: 463px; }
  .social-square {
    position: absolute; left: 489px; width: 34px; height: 34px; border-radius: 4px;
  }
  .social-square--photo { top: 116px; background: var(--orange); }
  .social-square--page { top: 160px; background: var(--blue); }

  /* Front side (portrait) */
  .card--front { left: 710px; top: 84px; width: 327px; height: 568px; }
  .front-lower {
    position: absolute; left: 0; right: 0; top: 284px; bottom: 0; background: var(--orange);
  }
  .front-rule {
    position: absolute; left: 0; right: 0; top: 278px; height: 3px; background: var(--blue);
  }
  .holder-name {
    position: absolute; top: 64px; width: 100%; text-align: center;
    font-family: "Share Tech Mono", monospace; font-weight: 400; font-size: 36px; color: var(--blue);
    letter-spacing: 1px;
  }
  .holder-role {
    position: absolute; top: 112px; width: 100%; text-align: center;
    font-family: "Share Tech Mono", monospace; font-size: 19px; color: var(--orange);
    letter-spacing: 1px;
  }
  .card--front .brand-mark { left: 163px; top: 186px; }
  .card--front .brand-name { color: var(--white); margin-top: 16px; }

  .contact {
    position: absolute; left: 0; right: 0; text-align: center;
    font-family: "Yanone Kaffeesatz", sans-serif; font-weight: 400;
    font-size: 18px; color: var(--white); line-height: 21px; letter-spacing: 0.5px;
  }
  .contact--address { top: 418px; }
  .contact--lines { top: 472px; line-height: 23px; }
  .contact .label { color: var(--ink); }
</style>
</head>
<body>

  <section class="card card--back" aria-label="Card back">
    <div class="brand-mark">
      <div class="brand-disc"></div>
      <div class="brand-name">Kestrel Bay<br>Wildlife Tours</div>
    </div>

    <div class="rotated prompt-title">TAKING PICTURES?</div>
    <div class="rotated prompt-line">TAG US IN YOUR PICTURES WITH:</div>
    <div class="rotated social-tag social-tag--hash">#kbwildtoursco</div>
    <div class="rotated social-tag social-tag--handle">@kbwildtoursco</div>

    <div class="social-square social-square--photo" role="img" aria-label="Photo sharing profile"></div>
    <div class="social-square social-square--page" role="img" aria-label="Social page"></div>
  </section>

  <section class="card card--front" aria-label="Card front">
    <div class="front-lower"></div>
    <div class="front-rule"></div>

    <h1 class="holder-name">Colin Marsby</h1>
    <div class="holder-role">DIRECTOR</div>

    <div class="brand-mark">
      <div class="brand-disc"></div>
      <div class="brand-name">Kestrel Bay Wildlife Tours</div>
    </div>

    <div class="contact contact--address">
      PO Box 71<br>Fennick Point NSW 2741
    </div>
    <div class="contact contact--lines">
      <span class="label">P:</span> +61 2 5550 4817<br>
      <span class="label">E:</span> info@kestrelbaywildtours.example<br>
      <span class="label">W:</span> www.kestrelbaywildtours.example
    </div>
  </section>

</body>
</html>
```